Wattlegrove Campus Lodgings needs a business card design

Hi Guys,

We are a Student Accommodation company in Australia. We already have a logo which I will submit.

I will require the design of the business cards from you.

I am after something that looks clean, modern and that people feel interested and actually want to contact us.

We would like to see designs that are innovative.

On the business cards I will require to have:

Employee Name
Position
Phone number
Email
Facebook page

I hope you can help me with this project guys as I have heard really good things from you.

```html
<!DOCTYPE html>
<html lang="en">
<head>
<meta charset="utf-8">
<title>Wattlegrove Campus Lodgings – Business Card</title>
<link rel="stylesheet" href="https://fonts.googleapis.com/css2?family=Fira+Sans:wght@400;600&display=swap">
<style>
  :root {
    --brand-green: #118e42;
    --brand-yellow: #fbc137;
    --card-white: #ffffff;
  }
  html, body {
    margin: 0;
    padding: 0;
    overflow: hidden;
    background: var(--card-white);
  }
  .card {
    position: relative;
    width: 1200px;
    height: 726px;
    background: var(--card-white);
    overflow: hidden;
    font-family: "Fira Sans", sans-serif;
  }
  .top-band {
    position: absolute;
    left: 0;
    top: 0;
    width: 100%;
    height: 54px;
    background: var(--brand-green);
  }
  .brand {
    position: absolute;
    left: 90px;
    top: 340px;
    display: flex;
    align-items: center;
    gap: 24px;
  }
  .brand-square {
    width: 110px;
    height: 110px;
    background: var(--brand-green);
  }
  .brand-name {
    margin: 0;
    color: var(--brand-green);
    font-weight: 600;
    font-size: 36px;
    line-height: 1.08;
    letter-spacing: 1px;
    text-transform: uppercase;
  }
  .contact-block {
    position: absolute;
    left: 590px;
    top: 292px;
  }
  .person-name {
    margin: 0;
    color: var(--brand-yellow);
    font-weight: 600;
    font-size: 50px;
    line-height: 1;
    letter-spacing: 0;
    text-transform: uppercase;
  }
  .person-role {
    margin: 4px 0 0;
    color: var(--brand-green);
    font-weight: 400;
    font-size: 28px;
    line-height: 34px;
  }
  .contact-list {
    list-style: none;
    margin: 30px 0 0;
    padding: 0;
    color: var(--brand-yellow);
    font-size: 27px;
    line-height: 31px;
  }
  .contact-list li {
    display: flex;
  }
  .contact-label {
    width: 47px;
    font-weight: 600;
  }
  .contact-value {
    font-weight: 400;
  }
</style>
</head>
<body>
  <main class="card">
    <div class="top-band"></div>

    <div class="brand">
      <div class="brand-square"></div>
      <p class="brand-name">Wattlegrove<br>Campus<br>Lodgings</p>
    </div>

    <section class="contact-block">
      <h1 class="person-name">Rowan Ashcombe</h1>
      <p class="person-role">National Sales Manager</p>
      <ul class="contact-list">
        <li><span class="contact-label">P.</span><span class="contact-value">08 9000 4417</span></li>
        <li><span class="contact-label">E.</span><span class="contact-value">rowan_ashcombe@wattlegrove.com.au</span></li>
        <li><span class="contact-label">F.</span><span class="contact-value">xxxx@yourpage.xxxxx</span></li>
      </ul>
    </section>
  </main>
</body>
</html>
```